Wine label Design

We are looking to develop an elegant contemporary Chilean design; for a new Wine Brand TORVENA to be sold in Chinese Market.
We would like to see designs that are a fine balance between having a traditional design that can offer quality reassurance and being distinctive enough to stand out on crowded shelves. The final design should be easy-to-remember and communicate Quality, Tradition and have a conection with Chile.

Target Market(s)

Urban Chinese between 25 to 40 yo

Requirements
Must have
• Paper label
Information on Front label : Grape (example Cabernet sauvignon) / Vintage (ex 2010) / Wine of Chile
Bottle shape is given (see attached)
Nice to have
• An element of uniqueness, easy to recall the brand
Red and Gold Color are appreciated by the Target
Should not have
• White background
Number 4 is considered death, should not be included on the design

```html
<!DOCTYPE html>
<html lang="en">
<head>
<meta charset="utf-8">
<title>TORVENA – Wine of Chile – Cabernet Sauvignon Label</title>
<link rel="stylesheet" href="https://fonts.googleapis.com/css2?family=Playfair+Display:wght@700;900&family=Yellowtail&display=swap">
<style>
  :root {
    --backdrop: #ececec;
    --label-red: #8a0202;
    --band-black: #161414;
    --brand-red: #e8141c;
    --tab-red: #e0141b;
    --ink: #141010;
    --gold-dark: #8a5a12;
    --gold-mid: #d8a544;
    --gold-light: #f6dc8a;
    --bloom-yellow: #f4d21c;
    --bloom-orange: #e8801c;
    --bloom-green: #b9cf54;
  }
  html, body {
    margin: 0;
    padding: 0;
    width: 1200px;
    height: 1000px;
    overflow: hidden;
    background: var(--backdrop);
  }
  .canvas {
    position: relative;
    width: 1200px;
    height: 1000px;
    background: radial-gradient(ellipse at center, #f7f7f7 0%, var(--backdrop) 70%, #dcdcdc 100%);
  }
  .label {
    position: absolute;
    left: 390px;
    top: 37px;
    width: 420px;
    height: 926px;
    background: var(--label-red);
    overflow: hidden;
    box-shadow: 0 2px 10px rgba(0,0,0,0.12);
  }
  .bloom {
    position: absolute;
    left: 0;
    top: 0;
    width: 420px;
    height: 926px;
  }
  .name-band {
    position: absolute;
    left: 0;
    top: 382px;
    width: 420px;
    height: 174px;
    background: var(--band-black);
  }
  .name-band::before,
  .name-band::after {
    content: "";
    position: absolute;
    left: 0;
    width: 100%;
    height: 7px;
    background: linear-gradient(90deg, var(--gold-dark), var(--gold-light) 35%, var(--gold-mid) 60%, var(--gold-light) 85%, var(--gold-dark));
  }
  .name-band::before { top: -3px; }
  .name-band::after { bottom: -3px; }
  .origin-tab {
    position: absolute;
    left: 115px;
    top: 350px;
    width: 199px;
    height: 46px;
    background: var(--tab-red);
    color: var(--ink);
    font-family: "Playfair Display", Georgia, serif;
    font-weight: 900;
    font-size: 27px;
    line-height: 46px;
    text-align: center;
    letter-spacing: -0.5px;
    transform: scaleX(0.86);
    z-index: 2;
  }
  .brand-name {
    position: absolute;
    left: 0;
    top: 405px;
    width: 420px;
    text-align: center;
    color: var(--brand-red);
    font-family: "Yellowtail", cursive;
    font-size: 84px;
    line-height: 120px;
    margin: 0;
    font-weight: 400;
  }
  .vintage {
    position: absolute;
    left: 388px;
    top: 782px;
    color: var(--ink);
    font-family: "Yellowtail", cursive;
    font-size: 24px;
    transform: translateX(-50%);
  }
  .vintage-rule {
    position: absolute;
    left: 230px;
    top: 813px;
    width: 180px;
    height: 2px;
    background: var(--ink);
  }
  .grape {
    position: absolute;
    left: 40px;
    top: 796px;
    margin: 0;
    color: var(--ink);
    font-family: "Yellowtail", cursive;
    font-weight: 400;
    font-size: 54px;
    line-height: 56px;
  }
  .grape span { display: block; }
  .grape .grape-second { padding-left: 70px; }
</style>
</head>
<body>
<main class="canvas">
  <section class="label">
    <svg class="bloom" viewBox="0 0 420 926" role="img" aria-label="Decorative bloom of gold, red, orange, yellow and green teardrop petals radiating from the left edge">
      <defs>
        <radialGradient id="bloomTone" cx="0.08" cy="0.5" r="0.62">
          <stop offset="0" stop-color="#9c6a1e"/>
          <stop offset="0.35" stop-color="#d0973a"/>
          <stop offset="0.6" stop-color="#e8b24a"/>
          <stop offset="0.8" stop-color="#e8801c"/>
          <stop offset="0.93" stop-color="#d9c24a"/>
          <stop offset="1" stop-color="#b84a1a"/>
        </radialGradient>
      </defs>
      <ellipse cx="30" cy="470" rx="318" ry="462" fill="url(#bloomTone)"/>
    </svg>
    <div class="name-band"></div>
    <div class="origin-tab">Wine of Chile</div>
    <h1 class="brand-name">TORVENA</h1>
    <div class="vintage">2010</div>
    <div class="vintage-rule"></div>
    <h2 class="grape"><span>Cabernet</span><span class="grape-second">Sauvignon</span></h2>
  </section>
</main>
</body>
</html>
```